Label Craft Beer with CBD

Create a label for our cbd (cannabidiol) beer. We do have a first / simple idea. now it needs a professional finish. Please show your very own idea as well, because ours is only a draft and we need YOUR HELP! size front: H 8 cm, W 7 cm size back: H 7.5 cm, W 5.5 cm

Niedrige Design-Qualität

```html
<!DOCTYPE html>
<html lang="en">
<head>
<meta charset="utf-8">
<title>Verda Brew – Label Front and Back</title>
<link rel="stylesheet" href="https://fonts.googleapis.com/css2?family=Oswald:wght@500;700&family=Playfair+Display:wght@400;700;900&display=swap">
<style>
  :root {
    --green: #4b5a28;
    --dark: #231815;
    --white: #ffffff;
    --page: #ffffff;
    --serif: "Playfair Display", Georgia, serif;
    --condensed: "Oswald", "Arial Narrow", sans-serif;
  }
  * { box-sizing: border-box; margin: 0; padding: 0; }
  html, body { width: 1200px; height: 1200px; overflow: hidden; background: var(--page); }
  .canvas { position: relative; width: 1200px; height: 1200px; }

  .side-title {
    position: absolute; font-family: var(--condensed); font-weight: 700;
    color: var(--green); font-size: 66px; line-height: 1; letter-spacing: 1px;
    transform: translateX(-50%);
  }
  .side-title--front { left: 334px; top: 196px; }
  .side-title--back { left: 942px; top: 218px; }

  .label { position: absolute; overflow: hidden; box-shadow: 0 26px 24px -18px rgba(0,0,0,.45); }
  .band { position: absolute; left: 0; width: 100%; }
  .band--green { background: var(--green); }
  .band--dark { background: var(--dark); }
  .rule { position: absolute; left: 0; width: 100%; height: 2px; background: var(--white); }

  /* Front label */
  .label--front { left: 55px; top: 277px; width: 560px; height: 637px; }
  .tag-cloudy {
    position: absolute; left: 209px; top: 13px; width: 134px; height: 22px;
    background: var(--dark); border: 1.5px solid var(--white); border-radius: 3px;
    color: var(--white); font-family: var(--serif); font-weight: 700; font-size: 12px;
    text-align: center; line-height: 19px;
  }
  .brand-seal {
    position: absolute; left: 193px; top: 35px; width: 172px; height: 172px;
    border-radius: 50%; background: var(--white);
    display: flex; align-items: center; justify-content: center;
  }
  .brand-seal__name {
    font-family: var(--serif); font-weight: 700; color: var(--dark);
    font-size: 25px; letter-spacing: 1px;
  }
  .product-name {
    position: absolute; left: 0; width: 100%; text-align: center; color: var(--white);
    font-family: var(--serif); line-height: 1;
  }
  .product-name--main { top: 238px; font-size: 98px; font-weight: 900; letter-spacing: 1px; }
  .product-name--sub { top: 325px; font-size: 82px; font-weight: 400; }

  .style-ribbon {
    position: absolute; left: 173px; top: 430px; width: 211px; height: 26px;
    background: var(--dark); color: var(--white); font-family: var(--serif); font-weight: 700;
    font-size: 16px; text-align: center; line-height: 26px;
    clip-path: polygon(0 50%, 6% 0, 94% 0, 100% 50%, 94% 100%, 6% 100%);
  }
  .origin-mark {
    position: absolute; display: flex; align-items: center; gap: 5px;
    font-family: var(--condensed); font-weight: 700; font-size: 8px; color: var(--white);
    transform: translateX(-50%);
  }
  .origin-mark__shield { width: 20px; height: 24px; }
  .origin-mark--front { left: 280px; top: 470px; }

  .facts { position: absolute; left: 0; top: 548px; width: 100%; height: 64px; }
  .fact {
    position: absolute; top: 0; width: 64px; height: 64px; margin-left: -32px;
    border: 2px solid var(--white); border-radius: 50%;
    display: flex; align-items: center; justify-content: center; text-align: center;
    color: var(--white); font-family: var(--condensed); font-weight: 500;
    font-size: 11px; line-height: 1.15;
  }
  .fact--small { font-size: 8px; }

  /* Back label */
  .label--back { left: 709px; top: 295px; width: 440px; height: 599px; }
  .back-title {
    position: absolute; left: 0; top: 58px; width: 100%; text-align: center;
    color: var(--white); font-family: var(--serif); font-weight: 900; font-size: 45px; line-height: 1;
    letter-spacing: 1px;
  }
  .barcode-slot {
    position: absolute; left: 17px; top: 177px; width: 72px; height: 243px;
    border: 2px solid var(--white);
    display: flex; align-items: center; justify-content: center;
  }
  .barcode-slot__text {
    transform: rotate(-90deg); color: var(--white); font-family: var(--serif);
    font-size: 30px; letter-spacing: 1px; white-space: nowrap;
  }
  .ingredients {
    position: absolute; left: 113px; top: 179px; width: 340px; height: 241px;
    border: 2px solid var(--white); padding: 26px 20px 0 20px;
    color: var(--white); font-family: var(--serif); font-weight: 700; font-size: 10px; line-height: 1.45;
  }
  .ingredients p { margin-bottom: 21px; }
  .ingredients p:nth-child(4) { margin-left: -4px; }
  .best-before {
    position: absolute; left: 60px; top: 451px; width: 140px; text-align: right;
    color: var(--white); font-family: var(--serif); font-weight: 700; line-height: 1.1;
  }
  .best-before__de { font-size: 6px; display: block; }
  .best-before__en { font-size: 8px; font-style: italic; display: block; }
  .best-before__field { position: absolute; left: 207px; top: 451px; width: 98px; height: 20px; background: var(--white); }
  .origin-mark--back { left: 221px; top: 500px; }
  .back-seal {
    position: absolute; left: 321px; top: 445px; width: 96px; height: 96px;
    border-radius: 50%; background: var(--white);
    display: flex; align-items: center; justify-content: center;
  }
  .back-seal .brand-seal__name { font-size: 14px; }
  .maker {
    position: absolute; left: 0; top: 551px; width: 100%; height: 48px; background: var(--green);
    color: var(--white); font-family: var(--serif); font-size: 11px; line-height: 1.3;
    text-align: center; padding-top: 10px;
  }
</style>
</head>
<body>
<main class="canvas">
  <h2 class="side-title side-title--front">FRONT</h2>
  <h2 class="side-title side-title--back">BACK</h2>

  <section class="label label--front" aria-label="Front label">
    <div class="band band--green" style="top:0;height:222px"></div>
    <div class="rule" style="top:222px"></div>
    <div class="band band--dark" style="top:226px;height:188px"></div>
    <div class="rule" style="top:414px"></div>
    <div class="band band--green" style="top:417px;height:112px"></div>
    <div class="band band--dark" style="top:529px;height:108px"></div>

    <div class="tag-cloudy">NATURTRÜB</div>
    <div class="brand-seal"><span class="brand-seal__name">KORVELLO</span></div>

    <h1 class="product-name product-name--main">VERDA</h1>
    <div class="product-name product-name--sub">BREW</div>

    <div class="style-ribbon">PREMIUM LAGER</div>
    <div class="origin-mark origin-mark--front">
      <span>SWISS</span>
      <svg class="origin-mark__shield" viewBox="0 0 20 24"><path d="M1 1h18v14l-9 8-9-8z" fill="none" stroke="#fff" stroke-width="2"/></svg>
      <span>MADE</span>
    </div>

    <div class="facts">
      <div class="fact" style="left:76px">10MG<br>CBD</div>
      <div class="fact" style="left:157px">4,3%<br>ALC</div>
      <div class="fact" style="left:239px">330<br>CL</div>
      <div class="fact" style="left:320px">WELL<br>BEING</div>
      <div class="fact fact--small" style="left:402px">NO<br>HANGOVER</div>
      <div class="fact" style="left:484px">NO<br>THC</div>
    </div>
  </section>

  <section class="label label--back" aria-label="Back label">
    <div class="band band--dark" style="top:0;height:39px"></div>
    <div class="rule" style="top:39px"></div>
    <div class="band band--green" style="top:41px;height:81px"></div>
    <div class="rule" style="top:122px"></div>
    <div class="band band--dark" style="top:124px;height:427px"></div>

    <h2 class="back-title">VERDA BREW</h2>

    <div class="barcode-slot"><span class="barcode-slot__text">BARCODE</span></div>

    <div class="ingredients">
      <p>ZUTATEN : wasser, gerstenmals, gerste,<br>hopfen, full spectrum hanfextrakt(pasteurisiert)</p>
      <p>INGRÉDIENTS: Eau, malt d'orge, orge, houblon,<br>full spectrum extrait de cannabis(pasteurisés)</p>
      <p>INGREDIENTI: acqua, orzo, malto, d'orzo, luppolo,<br>full spectrum estratto di cannabis(pastorizzato)</p>
      <p>INGREDIENTS: water, barley malt, barley,<br>hops, full spectrum cannabis extract(pasteurized)</p>
    </div>

    <div class="best-before">
      <span class="best-before__de">MINDESTENS HALTBAR BIS :</span>
      <span class="best-before__en">EXPIRY DATE :</span>
    </div>
    <div class="best-before__field"></div>

    <div class="origin-mark origin-mark--back">
      <span>SWISS</span>
      <svg class="origin-mark__shield" viewBox="0 0 20 24"><path d="M1 1h18v14l-9 8-9-8z" fill="none" stroke="#fff" stroke-width="2"/></svg>
      <span>MADE</span>
    </div>

    <div class="back-seal"><span class="brand-seal__name">KORVELLO</span></div>

    <footer class="maker">KORVELLO by feldmark ag, 6300 Talwil, Switzerland<br>www.korvello.swiss</footer>
  </section>
</main>
</body>
</html>
```